Corporate consulting business needs a business card

I want a professional business card.... surprise me

Updates

Reason: i dont think 2 days is enough

Target Market(s)

Corprorate and Not for Profit firms and organisations

Industry/Entity Type

Consulting

Contact Information for Business Card

Logo
Corporate Consulting Services
On Time, On Budget, Beyond Expectation
Tovan Presfield
Director
0427 31 94 62 (Larger)
tovan@tp-advisory.com.au
www.tp-advisory.com.au
include little icons beside the contact info:

- Envelope = email
- Phone = phone
- Globe = website

Font styles to use
Serif
Sans Serif

Requirements
Must have
• Professional and clean
Nice to have
• you tell me

```html
<!DOCTYPE html>
<html lang="en">
<head>
<meta charset="utf-8">
<title>TP Advisory – Business Card</title>
<link rel="stylesheet" href="https://fonts.googleapis.com/css2?family=Cinzel:wght@700&family=Montserrat:wght@500;700&display=swap">
<style>
  :root {
    --backdrop: #e8e5e1;
    --card: #ffffff;
    --band-grey: #56595b;
    --band-brown: #6b4a37;
    --brown: #6f4a36;
    --ink: #3b3b3b;
    --ink-soft: #555555;
    --hatch: #b9b6b2;
  }
  * { margin: 0; padding: 0; box-sizing: border-box; }
  html, body {
    width: 1200px; height: 801px; overflow: hidden;
    background: var(--backdrop);
  }
  .card {
    position: absolute; top: 273px;
    width: 480px; height: 266px;
    background: var(--card);
    overflow: hidden;
    box-shadow: 0 3px 10px rgba(0,0,0,0.18);
  }
  .card--front { left: 110px; }
  .card--back { left: 635px; }
  .band-top { position: absolute; left: 0; top: 0; width: 100%; height: 29px; background: var(--band-grey); }
  .band-bottom { position: absolute; left: 0; bottom: 0; width: 100%; height: 27px; background: var(--band-brown); }

  .brand-name {
    position: absolute;
    font-family: "Cinzel", serif; font-weight: 700;
    color: var(--brown); white-space: nowrap;
    text-align: center; letter-spacing: 1px;
  }
  .brand-line {
    position: absolute;
    font-family: "Cinzel", serif; font-weight: 700;
    color: var(--ink); white-space: nowrap;
    text-align: center; letter-spacing: 0.3px;
  }

  .card--front .brand-name { left: 142px; width: 200px; top: 100px; font-size: 30px; }
  .card--front .brand-line { left: 142px; width: 200px; top: 163px; font-size: 15px; }
  .hatch-line {
    position: absolute; left: 153px; top: 224px; width: 184px; height: 6px;
    background: repeating-linear-gradient(120deg, var(--hatch) 0 1px, transparent 1px 4px);
  }

  .card--back .brand-name { left: 10px; width: 172px; top: 97px; font-size: 24px; }
  .card--back .brand-line { left: 10px; width: 172px; top: 153px; font-size: 12.5px; }
  .divider {
    position: absolute; left: 243px; top: 56px; width: 6px; height: 154px;
    background: repeating-linear-gradient(150deg, var(--hatch) 0 1px, transparent 1px 4px);
  }

  .contact { position: absolute; left: 271px; top: 58px; width: 180px; font-family: "Montserrat", sans-serif; }
  .contact__name { font-weight: 700; font-size: 14px; color: var(--ink); letter-spacing: 0.6px; }
  .contact__role { font-weight: 500; font-size: 8.5px; color: var(--ink-soft); letter-spacing: 0.4px; }
  .contact__rule { height: 2px; background: var(--brown); width: 175px; margin-top: 4px; }
  .contact__row { display: flex; align-items: center; gap: 14px; position: absolute; left: 0; }
  .contact__row--phone { top: 55px; }
  .contact__row--web { top: 88px; }
  .icon { width: 24px; height: 26px; flex: none; }
  .contact__text { font-weight: 500; font-size: 11.5px; color: var(--ink-soft); line-height: 15px; white-space: nowrap; }
  .contact__text--phone { font-size: 12.5px; letter-spacing: 0.5px; }
</style>
</head>
<body>

<section class="card card--front">
  <div class="band-top"></div>
  <div class="brand-name">TP ADVISORY</div>
  <div class="brand-line">CONSULTING SERVICES</div>
  <div class="hatch-line"></div>
  <div class="band-bottom"></div>
</section>

<section class="card card--back">
  <div class="band-top"></div>
  <div class="brand-name">TP ADVISORY</div>
  <div class="brand-line">CONSULTING SERVICES</div>
  <div class="divider"></div>

  <div class="contact">
    <div class="contact__name">TOVAN PRESFIELD</div>
    <div class="contact__role">DIRECTOR</div>
    <div class="contact__rule"></div>

    <div class="contact__row contact__row--phone">
      <svg class="icon" viewBox="0 0 24 26" aria-hidden="true">
        <path d="M2 2h20v18l-10 5-10-5z" fill="#6f4a36"/>
        <path d="M7.5 7c1-.8 2 .1 2.4 1l.5 1.2c.2.6-.3 1-.7 1.3.6 1.4 1.5 2.4 2.8 3 .3-.4.8-.9 1.3-.6l1.2.6c.9.4 1.6 1.3.8 2.3-1.5 1.5-4 .3-5.8-1.6C8.2 12.3 6.2 9 7.5 7z" fill="#fff"/>
      </svg>
      <div class="contact__text contact__text--phone">0427 31 94 62</div>
    </div>

    <div class="contact__row contact__row--web">
      <svg class="icon" viewBox="0 0 24 26" aria-hidden="true">
        <path d="M2 2h20v18l-10 5-10-5z" fill="#6f4a36"/>
        <circle cx="12" cy="11.5" r="5.5" fill="none" stroke="#fff" stroke-width="1.3"/>
        <ellipse cx="12" cy="11.5" rx="2.3" ry="5.5" fill="none" stroke="#fff" stroke-width="1"/>
        <path d="M6.5 11.5h11" stroke="#fff" stroke-width="1"/>
      </svg>
      <div class="contact__text">tovan@tp-advisory.com.au<br>www.tp-advisory.com.au</div>
    </div>
  </div>

  <div class="band-bottom"></div>
</section>

</body>
</html>
```